We are a General Practice - Family medicine
We also have Allied Health professionals working within our team

Industry/Entity Type

Business

Contact Information for Business Card

Front of the card to display:

HARBOURVIEW MEDICAL
PHONE 6381 2947

5/14 Kellerton Avenue
Launceston Tasmania 7268

Back of the card to display:

My Appointments
Date:
Time:
With:

Please remember to phone us on 6381 2947 to cancel your appointment if you can't keep it.
A fee applied to missed appointments

```html
<!DOCTYPE html>
<html lang="en">
<head>
<meta charset="utf-8">
<title>Harbourview Medical – Business Card</title>
<link rel="stylesheet" href="https://fonts.googleapis.com/css2?family=Arimo:wght@400;700&display=swap">
<style>
  :root {
    --page-bg: #e9e6e1;
    --card-bg: #ffffff;
    --ink-grey: #6d6e70;
    --brand-blue: #29a3dc;
    --brand-green: #8cc63f;
    --line-blue: #4fb3e3;
    --text-white: #ffffff;
    --shadow: rgba(0, 0, 0, 0.25);
  }
  * { margin: 0; padding: 0; box-sizing: border-box; }
  html, body {
    width: 1000px;
    height: 1200px;
    overflow: hidden;
    background: var(--page-bg);
    font-family: "Arimo", Arial, sans-serif;
  }
  .canvas { position: relative; width: 1000px; height: 1200px; }

  .card {
    position: absolute;
    left: 95px;
    width: 813px;
    height: 485px;
    background: var(--card-bg);
    border-radius: 24px;
    box-shadow: 0 6px 18px var(--shadow);
    overflow: hidden;
  }
  .card--front { top: 95px; }
  .card--back { top: 651px; }

  /* Front */
  .brand-name {
    position: absolute;
    top: 175px;
    left: 0;
    width: 100%;
    text-align: center;
    font-size: 50px;
    font-weight: 400;
    color: var(--brand-blue);
    letter-spacing: -0.5px;
  }
  .holder-name {
    position: absolute;
    left: 45px;
    top: 334px;
    font-size: 28px;
    font-weight: 700;
    color: var(--ink-grey);
  }
  .holder-rule {
    position: absolute;
    left: 300px;
    right: 41px;
    top: 351px;
    height: 2px;
    background: var(--brand-green);
  }
  .holder-title {
    position: absolute;
    left: 46px;
    top: 371px;
    font-size: 22px;
    color: var(--brand-green);
  }
  .address {
    position: absolute;
    left: 46px;
    top: 408px;
    font-size: 20px;
    line-height: 27px;
    color: var(--brand-blue);
  }
  .phone {
    position: absolute;
    right: 41px;
    top: 362px;
    display: flex;
    align-items: center;
    gap: 8px;
    font-size: 22px;
    font-weight: 700;
    color: var(--ink-grey);
  }
  .phone svg { width: 22px; height: 18px; }

  /* Back */
  .appointments-title {
    position: absolute;
    top: 42px;
    width: 100%;
    text-align: center;
    font-size: 23px;
    color: var(--ink-grey);
  }
  .field {
    position: absolute;
    left: 58px;
    right: 54px;
    display: flex;
    align-items: flex-end;
    gap: 20px;
  }
  .field__label {
    width: 46px;
    font-size: 20px;
    color: var(--ink-grey);
    line-height: 1;
  }
  .field__line {
    flex: 1;
    height: 2px;
    background: var(--line-blue);
    margin-bottom: 2px;
  }
  .field--date { top: 129px; }
  .field--time { top: 181px; }
  .field--with { top: 232px; }

  .notice-band {
    position: absolute;
    left: 0;
    right: 0;
    bottom: 0;
    height: 205px;
    background: linear-gradient(to bottom, rgba(140, 198, 63, 0) 0%, rgba(140, 198, 63, 0.75) 40%, var(--brand-green) 60%);
  }
  .notice {
    position: absolute;
    left: 0;
    right: 0;
    bottom: 14px;
    text-align: center;
    color: var(--text-white);
  }
  .notice__main { font-size: 20px; line-height: 25px; }
  .notice__fee { font-size: 18px; line-height: 28px; }
</style>
</head>
<body>
<div class="canvas">

  <section class="card card--front" aria-label="Business card front">
    <div class="brand-name">Harbourview Medical</div>

    <div class="holder-name">Your name here</div>
    <div class="holder-rule"></div>
    <div class="holder-title">Title here</div>

    <div class="address">
      5/14 Kellerton Avenue<br>
      Launceston Tasmania 7268
    </div>

    <div class="phone">
      <svg viewBox="0 0 22 18" aria-hidden="true">
        <path fill="#8cc63f" d="M2 6c0-3 4-4 9-4s9 1 9 4v2h-5V6H7v2H2z"/>
        <path fill="#8cc63f" d="M6 9h10l3 7H3z"/>
        <circle cx="11" cy="12.5" r="2" fill="#ffffff"/>
      </svg>
      <span>6381 2947</span>
    </div>
  </section>

  <section class="card card--back" aria-label="Business card back">
    <div class="appointments-title">My Appointments</div>

    <div class="field field--date"><span class="field__label">Date</span><span class="field__line"></span></div>
    <div class="field field--time"><span class="field__label">Time</span><span class="field__line"></span></div>
    <div class="field field--with"><span class="field__label">With</span><span class="field__line"></span></div>

    <div class="notice-band"></div>
    <div class="notice">
      <p class="notice__main">Please remember to phone us on 6381 2947 to cancel your appointment<br>if you can't keep it.</p>
      <p class="notice__fee">A fee applied to missed appointments</p>
    </div>
  </section>

</div>
</body>
</html>
```